Modern and sophisticated web design for architect/designer

Lumo Vant is a Building Design & Drafting studio based in Nedlands Western Australia, providing a high quality and complete client service from concept design through Council planning approvals and building licenses to construction drawings for kitchens and bathrooms, extensions, additions, renovations and new homes.

Lumo Vant is looking for a new qwerty design that *is different from a normal* 2/3 column website. The website design must be very arty, clean and catchy. This design needs to be very different and must not look like a downloadable template.

The design must be able to display a lot of photos for the different projects.

The design must comply with W3C standards (i.e. use of fonts) and must be delivered to us in A PSD layered format.

Here are a couple of example website designs that exemplify what I am after:
1) http://www.prtd.com.au/
2) http://www.martinholsbyarchitect.com/en/
3) http://veromiks.com/

I particularly like numbers 1 and 2. The third, Veromiks, jumps around a little between pages as it is actually several companies. I prefer the page design to remain steady if possible.

I like the very clever nature of number 1 (PRTD). It captures the interest, although slightly gimmicky, however I think it doesn't overpower. Its modern, and visual.

I like the clean elegant design of number 2 (Holsby), it simply delivers everything necessary in a clear intelligent manner, its attractive, menu is clever simple to use and attractive.

I would be very happy to have either of these websites.

here is another one:
4) http://www.tqarchitect.com.au/

Although this is similarly elegant, it appears quite dated. I don't like the thumbnails that you click on in the gallery, its quite clumsy. It looks minimalist, and IS minimalist, doesn't look like there is much option to expand other than changing the pictures.

If you look at my own website:
http://www.lumovant.com.au

I designed and built it myself without any skills or experience. I had to use a generic photo album generator which was worse than useless, the point I am trying to make is I tried to make the menu system a little unusual, I tried to keep the pages neat and tidy, and totally used the "black website" method. However I am more inclined to go with the lighter/white pages of (1) and (2) above because they tend to show photos better.

Dear Designers. 

ArtHive Administration has worked to provide a more comprehensive brief. Please review the amended description. 

Kind Regards, Wesley. 

Target Market(s)

Target market is people who are looking to renovate their home

Industry/Entity Type

Construction

Requirements
Must have
• The brief is to design a visual modern, elegant, sophisticated website for a small scale designer/photographer/architect that looks itself like it is designed. Not off the shelf, simple and dated. Basically the design itself has to exemplify me, it has to say "this guy is a designer, and he is good at it".

```html
<!DOCTYPE html>
<html lang="en">
<head>
<meta charset="utf-8">
<title>Lumo Vant — Building Design &amp; Drafting Studio</title>
<link rel="stylesheet" href="https://fonts.googleapis.com/css2?family=Oswald:wght@300;400&family=Poiret+One&display=swap">
<style>
  :root {
    --ink: #000000;
    --paper: #ffffff;
    --mondrian-yellow: #ffff00;
    --mondrian-red: #e00e12;
    --mondrian-blue: #2121c6;
    --headline-yellow: #f4ef3a;
    --footer-grey: #d8d8d8;
    --rule-grey: #666666;
  }
  * { box-sizing: border-box; margin: 0; padding: 0; }
  html, body { width: 1200px; height: 1053px; overflow: hidden; background: var(--ink); }
  body { position: relative; font-family: Arial, Helvetica, sans-serif; }
  .tile { position: absolute; }

  .photo-house { left: 0; top: 0; width: 469px; height: 204px;
    background: linear-gradient(180deg, #4f86c4 0%, #9fb8c9 45%, #8a8a80 75%, #4c5a3e 100%); }
  .photo-pavilion { left: 0; top: 212px; width: 344px; height: 496px;
    background: linear-gradient(180deg, #8aa4c8 0%, #d5d9e0 40%, #9a9fb0 65%, #5a5f72 100%); }
  .photo-kitchen { left: 651px; top: 0; width: 549px; height: 222px;
    background: linear-gradient(135deg, #5a3a2a 0%, #8a5a3c 40%, #d8d0c0 70%, #6a5a4a 100%); }
  .photo-facade { left: 489px; top: 433px; width: 179px; height: 328px;
    background: linear-gradient(180deg, #7fa3d4 0%, #c9bfae 35%, #8f877c 70%, #4b5a3a 100%); }
  .photo-deck { left: 899px; top: 367px; width: 301px; height: 342px;
    background: linear-gradient(180deg, #f4f4f2 0%, #b89a6a 40%, #6a4a2e 70%, #3a3228 100%); }

  .block-yellow { background: var(--mondrian-yellow); }
  .block-red { background: var(--mondrian-red); }
  .block-blue { background: var(--mondrian-blue); }

  .main-nav { left: 489px; top: 18px; width: 152px; height: 337px; padding: 14px 0 0 26px; }
  .main-nav a { display: block; font-family: "Oswald", sans-serif; font-weight: 300;
    font-size: 32px; line-height: 35px; color: var(--ink); text-decoration: none; transform: scaleX(.92); transform-origin: left; }

  .intro { left: 355px; top: 212px; width: 114px; height: 496px; padding: 212px 6px 0 10px;
    color: var(--paper); font-size: 13px; line-height: 16px; }

  .tagline { left: 651px; top: 230px; width: 549px; height: 125px; padding: 9px 0 0 118px;
    font-family: "Poiret One", sans-serif; font-size: 49px; line-height: 59px; color: var(--headline-yellow); }

  .brand-band { left: 355px; top: 272px; width: 282px; height: 28px; background: var(--paper);
    font-family: "Oswald", sans-serif; font-weight: 400; font-size: 24px; line-height: 28px;
    letter-spacing: 6px; color: var(--ink); padding-left: 10px; }
  .brand-sub { left: 489px; top: 367px; width: 400px; height: 55px; background: var(--paper);
    font-family: "Oswald", sans-serif; font-weight: 400; font-size: 30px; line-height: 55px;
    letter-spacing: 6px; color: var(--ink); padding-left: 84px; }

  .footer-nav { left: 17px; top: 893px; font-size: 15px; color: var(--paper); }
  .footer-nav a { color: var(--paper); text-decoration: none; }
  .footer-nav span { margin: 0 7px; }
  .copyright { left: 19px; top: 916px; font-size: 12.5px; color: var(--mondrian-yellow); }
  .footer-brand { left: 19px; top: 940px; font-family: "Oswald", sans-serif; font-weight: 400;
    font-size: 16px; line-height: 20px; letter-spacing: 3px; color: var(--mondrian-red); }

  .contact { right: 23px; top: 893px; text-align: right; font-size: 14.5px; line-height: 18px; color: var(--footer-grey); font-style: normal; }
  .footer-rule { left: 1005px; top: 974px; width: 172px; height: 1px; background: var(--rule-grey); }
  .social { left: 1004px; top: 988px; display: flex; gap: 5px; }
  .social a { width: 39px; height: 39px; display: block; }
  .social .s1 { background: #3b3a8f; }
  .social .s2 { background: #2f8de0; }
  .social .s3 { background: #1f5fa8; }
  .social .s4 { background: #d8231c; }
</style>
</head>
<body>
  <div class="tile photo-house" role="img" aria-label="Photo of a modern two-storey house with timber-framed glazing"></div>
  <div class="tile photo-pavilion" role="img" aria-label="Rendering of a sail-roofed pavilion reflected in water"></div>
  <div class="tile photo-kitchen" role="img" aria-label="Photo of a renovated kitchen with stone benchtops and timber floor"></div>

  <nav class="tile main-nav block-yellow">
    <a href="#">HOME</a><a href="#">ABOUT</a><a href="#">SERVICES</a><a href="#">PROJECTS</a><a href="#">CONTACT</a>
  </nav>

  <div class="tile intro block-red">
    <p>Providing a high quality and complete client service from concept design through Council planning approvals and building licenses to construction drawings for kitchens and bathrooms, extensions, additions, renovations and new homes.</p>
  </div>

  <h1 class="tile tagline block-blue">Building Design &amp;<br>Drafting studio</h1>

  <div class="tile brand-band">LUMO VANT</div>
  <div class="tile brand-sub">DESIGN</div>

  <div class="tile photo-facade" role="img" aria-label="Photo of a rendered townhouse facade with balcony"></div>
  <div class="tile block-yellow" style="left:673px;top:433px;width:93px;height:116px"></div>
  <div class="tile block-red" style="left:673px;top:562px;width:93px;height:200px"></div>
  <div class="tile block-blue" style="left:780px;top:433px;width:109px;height:276px"></div>
  <div class="tile photo-deck" role="img" aria-label="Photo of a lit timber deck at dusk beside a house"></div>

  <nav class="tile footer-nav">
    <a href="#">HOME</a><span>|</span><a href="#">ABOUT</a><span>|</span><a href="#">SERVICES</a><span>|</span><a href="#">PROJECTS</a><span>|</span><a href="#">CONTACT</a>
  </nav>
  <p class="tile copyright">Copyright © 2013 LUMOVANT DESIGN. All rights reserved.</p>
  <div class="tile footer-brand">LUMO VANT<br>DESIGN</div>

  <address class="tile contact">
    Lot 18, 62 Larkmere Street,<br>
    Melbourne, VIC 3000, AU<br>
    tel: +01 555 01842<br>
    fax:+01 555 01843
  </address>
  <div class="tile footer-rule"></div>
  <div class="tile social">
    <a class="s1" href="#" aria-label="Social profile one"></a>
    <a class="s2" href="#" aria-label="Social profile two"></a>
    <a class="s3" href="#" aria-label="Social profile three"></a>
    <a class="s4" href="#" aria-label="Social profile four"></a>
  </div>
</body>
</html>
```